Meridale Hair Studio Needs a new appointment business card

We need a new appointment card for our hair salon.

I Dont want bright out there colours.
I would like it to be neat, clean, easy to read. White, Black, with a hint of colour if needed.

We need
-Logo
-Phone number 47260385
-Mobile Number: 0417360528
Address: Shop 3/217 Tarrow Street, Kelby Court, Brindell 4812

BACK SIDE OF CARD
- Appointment Time & Date (White background so we are able to write on it)
(If you are unable to make your appointment please contact us ASAP 47260385)

I also would like the chatterly and Snapfold logo(Find us on Chatterly)(find us on Snapfold)

Target Market(s)

appointment card simple to read. all information for their next appoint For all our clients male and female

Industry/Entity Type

Hairdresser

Contact Information for Business Card

-Logo
-Phone number 47260385

BACK SIDE OF CARD

Font styles to use
Serif
Sans Serif
Script

Requirements
Must have
• White Back ground on backside with appointment deatils so we are able to write information (like appointment time and date)
Nice to have
• Find us on Chatterly
and
snapfold - meridale_hairstudio
Should not have
• BRIGHT COLOURS

```html
<!DOCTYPE html>
<html lang="en">
<head>
<meta charset="utf-8">
<title>Meridale Hair Studio – Appointment Card</title>
<link rel="stylesheet" href="https://fonts.googleapis.com/css2?family=Marcellus&family=Roboto:wght@400;500;700&display=swap">
<style>
  :root {
    --backdrop: #3b3431;
    --card: #ffffff;
    --ink: #1d1d1d;
    --ink-soft: #444444;
    --rule: #222222;
    --art-from: #d9d9d9;
    --art-to: #8a8a8a;
  }
  * { box-sizing: border-box; margin: 0; padding: 0; }
  html, body {
    width: 1200px; height: 716px; overflow: hidden;
    background: var(--backdrop);
  }
  .canvas {
    position: relative; width: 1200px; height: 716px;
    display: flex; align-items: center; justify-content: center; gap: 40px;
  }
  .card {
    position: relative; width: 540px; height: 309px;
    background: var(--card); color: var(--ink);
    font-family: "Roboto", sans-serif;
    box-shadow: 0 10px 24px rgba(0,0,0,.45);
    overflow: hidden;
  }
  .brand {
    position: absolute;
    font-family: "Marcellus", serif;
    color: var(--ink);
    line-height: 1;
  }
  .brand-name { font-size: 30px; letter-spacing: 1px; text-transform: uppercase; }
  .brand-sub { font-size: 11px; letter-spacing: 4px; text-transform: uppercase; margin-top: 4px; text-align: right; }

  /* front */
  .card-front .brand { left: 36px; top: 36px; }
  .contact { position: absolute; left: 36px; top: 120px; font-size: 13px; line-height: 1.5; color: var(--ink-soft); }
  .contact-line { display: flex; align-items: center; gap: 6px; }
  .contact-line svg { width: 10px; height: 10px; flex: none; }
  .address { margin-top: 4px; }
  .social { position: absolute; left: 36px; bottom: 28px; display: flex; gap: 16px; font-size: 11px; color: var(--ink-soft); }
  .social-item { display: flex; align-items: center; gap: 6px; }
  .social-dot { width: 14px; height: 14px; border: 1.3px solid var(--ink); border-radius: 50%; }
  .card-front .shears { right: 0; top: 110px; width: 170px; height: 199px; }

  /* back */
  .card-back .shears { left: 0; top: 0; width: 120px; height: 260px; }
  .card-back .brand { right: 36px; top: 108px; }
  .appointment { position: absolute; left: 150px; top: 130px; font-size: 14px; font-weight: 500; }
  .field-row { position: absolute; left: 145px; right: 36px; top: 178px; display: flex; gap: 8px; font-size: 13px; }
  .field { display: flex; align-items: flex-end; flex: 1; gap: 4px; }
  .field-line { flex: 1; border-bottom: 1px solid var(--rule); height: 14px; }
  .notice { position: absolute; left: 170px; top: 228px; font-size: 16px; font-weight: 700; }

  .shears {
    position: absolute;
    background: linear-gradient(135deg, var(--art-from), var(--art-to));
    opacity: .55;
  }
</style>
</head>
<body>
<main class="canvas">
  <section class="card card-front" aria-label="Card front">
    <div class="brand">
      <div class="brand-name">Meridale</div>
      <div class="brand-sub">Hair Studio</div>
    </div>
    <div class="contact">
      <div class="contact-line">
        <svg viewBox="0 0 10 10" aria-hidden="true"><path d="M2 1 L4 1 L4.6 3 L3.4 3.8 Q4.5 6 6.2 6.6 L7 5.4 L9 6 L9 8 Q5 9 2.5 6 Q1 4 2 1Z" fill="#1d1d1d"/></svg>
        <span>47260385</span>
      </div>
      <div class="contact-line">
        <svg viewBox="0 0 10 10" aria-hidden="true"><rect x="2.5" y="0.5" width="5" height="9" rx="1" fill="none" stroke="#1d1d1d" stroke-width="1"/></svg>
        <span>0417360528</span>
      </div>
      <div class="address">Shop 3/217 Tarrow Street,<br>Kelby Court, Brindell 4812</div>
    </div>
    <div class="social">
      <div class="social-item"><span class="social-dot"></span>Chatterly</div>
      <div class="social-item"><span class="social-dot"></span>Snapfold</div>
    </div>
    <div class="shears" role="img" aria-label="Large open scissors illustration"></div>
  </section>

  <section class="card card-back" aria-label="Card back">
    <div class="shears" role="img" aria-label="Large open scissors illustration"></div>
    <div class="brand">
      <div class="brand-name">Meridale</div>
      <div class="brand-sub">Hair Studio</div>
    </div>
    <div class="appointment">Appointment</div>
    <div class="field-row">
      <div class="field">Time:<span class="field-line"></span></div>
      <div class="field">Date:<span class="field-line"></span></div>
    </div>
    <div class="notice">Contact us ASAP 47260385</div>
  </section>
</main>
</body>
</html>
```